Email signature design - law firm

We are a small boutique law firm which is located near the beach in Manly, Australia.

We have just recently developed a new logo and are looking to redesign our letterhead, business cards and email signatures.

This brief is for our email signatures. This is an email signature to appear at the bottom of our Outlook emails so we would like it to be text that we are able to edit as the wording in our email signature often required amendments.

I have attached a word document which had our new logo, and our previous email signature which all the information/wording that needs to be included.

We would like multiple designs with a modern, simplistic yet striking look.

Thanks.

font - raleway or montserrat

Need extra days to review

• Must have the exact wording which appears in the email signature in the word document attached to brief.
• Must be able to edit the text as it is for an Outlook email signature which wording will change from time to time.

```html
<!DOCTYPE html>
<html lang="en">
<head>
<meta charset="utf-8">
<title>Email Signature – Harwell &amp; Partners</title>
<link rel="stylesheet" href="https://fonts.googleapis.com/css2?family=Montserrat:ital,wght@0,300;0,400;0,500;0,600;0,700;1,400&display=swap">
<style>
  :root {
    --navy: #2e3d8a;
    --ink-blue: #2f4190;
    --rule-blue: #6e83c8;
    --text: #2b2b2b;
    --muted: #3a3a3a;
    --paper: #ffffff;
  }
  * { margin: 0; padding: 0; box-sizing: border-box; }
  html, body {
    width: 1200px;
    height: 515px;
    overflow: hidden;
    background: var(--paper);
  }
  body {
    font-family: "Montserrat", Arial, sans-serif;
    color: var(--text);
  }
  .signature {
    position: relative;
    width: 1200px;
    height: 515px;
    background: var(--paper);
  }
  .sign-off {
    position: absolute;
    left: 50px;
    top: 44px;
    font-size: 17px;
    font-weight: 300;
    color: var(--muted);
  }
  .sender-name {
    position: absolute;
    left: 49px;
    top: 68px;
    font-size: 30px;
    font-weight: 600;
    color: var(--ink-blue);
    letter-spacing: 0.2px;
  }
  .firm-name {
    position: absolute;
    right: 48px;
    top: 112px;
    font-size: 15px;
    font-weight: 700;
    color: var(--text);
    letter-spacing: 1px;
  }
  .contact-list {
    position: absolute;
    right: 48px;
    top: 168px;
    list-style: none;
    text-align: right;
  }
  .contact-item {
    display: flex;
    justify-content: flex-end;
    align-items: center;
    gap: 7px;
    height: 26px;
    font-size: 18px;
    font-weight: 300;
    color: var(--text);
  }
  .contact-icon {
    width: 17px;
    height: 17px;
    fill: var(--navy);
    flex: none;
  }
  .divider {
    position: absolute;
    left: 50px;
    right: 48px;
    top: 289px;
    height: 3px;
    background: var(--rule-blue);
  }
  .legal {
    position: absolute;
    left: 46px;
    right: 48px;
    font-size: 10.4px;
    line-height: 17px;
    color: var(--muted);
    text-align: justify;
  }
  .legal-label {
    font-style: italic;
    color: var(--ink-blue);
  }
  .privilege-note { top: 317px; }
  .liability-note {
    top: 383px;
    font-size: 13px;
    font-style: italic;
    color: var(--ink-blue);
    text-align: left;
    white-space: nowrap;
  }
  .fraud-note { top: 420px; }
  .footer-band {
    position: absolute;
    left: 0;
    right: 0;
    bottom: 0;
    height: 19px;
    background: var(--navy);
  }
</style>
</head>
<body>
<div class="signature">
  <p class="sign-off">Kindest regards,</p>
  <p class="sender-name">Naomi Castell</p>

  <p class="firm-name">Harwell &amp; Partners</p>

  <ul class="contact-list">
    <li class="contact-item">
      <span>(02) 9000 4811</span>
      <svg class="contact-icon" viewBox="0 0 24 24" aria-label="Phone">
        <path d="M2 9c0-3 4-5 10-5s10 2 10 5v2h-5V8.5c-1.5-.6-3.2-.9-5-.9s-3.5.3-5 .9V11H2z"/>
        <path d="M6 12l2-3h8l2 3v8H6z"/>
        <circle cx="12" cy="15.5" r="2.4" fill="#fff"/>
      </svg>
    </li>
    <li class="contact-item">
      <span>(02) 9000 4812</span>
      <svg class="contact-icon" viewBox="0 0 24 24" aria-label="Fax">
        <rect x="6" y="2" width="12" height="6" rx="1"/>
        <rect x="2" y="9" width="20" height="9" rx="2"/>
        <rect x="6" y="14" width="12" height="8" rx="1" fill="#fff" stroke="var(--navy)" stroke-width="2"/>
      </svg>
    </li>
    <li class="contact-item">
      <span>www.harwellpartners.com.au</span>
      <svg class="contact-icon" viewBox="0 0 24 24" aria-label="Website">
        <circle cx="12" cy="12" r="10"/>
        <g fill="none" stroke="#fff" stroke-width="1.4">
          <ellipse cx="12" cy="12" rx="4.5" ry="10"/>
          <line x1="12" y1="2" x2="12" y2="22"/>
          <line x1="2" y1="12" x2="22" y2="12"/>
          <path d="M4 7h16M4 17h16"/>
        </g>
      </svg>
    </li>
    <li class="contact-item">
      <span>Suite 4, 12 Coral Lane SEAVIEW NSW 2000</span>
    </li>
  </ul>

  <div class="divider"></div>

  <p class="legal privilege-note"><span class="legal-label">Important note:</span> This E-Mail and any attachment is PRIVILEGED and confidential. It must not be read, copied, disclosed or used by any person other than the above named addressees. In order to preserve the intended confidentiality and privilege, please notify us immediately if you have received this e-mail by mistake and secure-delete this e-mail from your system. Unauthorised perusal, use, disclosure, forwarding or copying is strictly prohibited and may be unlawful.</p>

  <p class="legal liability-note">Liability limited by a scheme approved under Professional Standards Legislation. Legal practitioners at HarbourLaw (NSW) Pty Ltd are members of the scheme.</p>

  <p class="legal fraud-note"><span class="legal-label">Fraud warning:</span> Please be aware that there is a significant risk posed by cyber fraud, specifically relating to email accounts and bank account details. Our bank account details will never change during the course of a transaction, and we will never advise you of a change to our bank details via email. Please check account details with us in person or by phone before making payments. If you advise us of your bank account details by email, please also ring and confirm the bank account details by phone as well.</p>

  <div class="footer-band"></div>
</div>
</body>
</html>
```